Corwick Habitat Web

We just need an update/re-design of our existing web site that would include our new company logo and some new photo's. Our current web site can be viewed at www.corwickhabitat.com.au. We would require something very similar to what we have at the moment in terms of content it should all be the same.
The web site would basically act more as a portfolio than one that would generate more business.
We are after a very modern and simple design and maybe something where we can upload our own project photo's and project descriptions as we complete them.

Industry/Entity Type

It Company

```html
<!DOCTYPE html>
<html lang="en">
<head>
<meta charset="utf-8">
<title>Corwick Habitat</title>
<link href="https://fonts.googleapis.com/css2?family=Open+Sans:wght@300;400&display=swap" rel="stylesheet">
<style>
:root{
  --teal:#468a8e;
  --teal-text:#3f8a8c;
  --ink:#2f2f2f;
  --grey:#7a7a7a;
  --rule:#c9c9c9;
  --btn:#e4e4e4;
  --btn-border:#b9b9b9;
  --bg:#ffffff;
}
*{margin:0;padding:0;box-sizing:border-box}
html,body{width:966px;height:1200px;overflow:hidden;background:var(--bg)}
body{position:relative;font-family:"Open Sans",sans-serif;color:var(--ink)}
.abs{position:absolute}
.brand{left:66px;top:22px;font-weight:300;font-size:36px;color:#3a3a3a;letter-spacing:.5px}
.contact{left:753px;font-size:12px;color:#222;display:flex;align-items:center;gap:8px}
.nav{left:0;top:89px;width:966px;height:34px;background:var(--teal)}
.nav a{position:absolute;top:10px;font-size:11.5px;color:#fff;text-decoration:none}
.nav .sep{position:absolute;top:12px;width:1px;height:12px;background:#8fbfc1}
.nav .active-mark{position:absolute;left:68px;top:34px;width:0;height:0;border-left:7px solid transparent;border-right:7px solid transparent;border-top:7px solid #fff;transform:rotate(180deg);top:117px}
.search{left:755px;top:97px;width:179px;height:17px;border:1px solid #7db0b2;background:var(--teal)}
.search span{position:absolute;left:5px;top:1px;font-size:9.5px;color:#a8cfd0}
.search .go{position:absolute;right:0;top:0;width:19px;height:15px;background:#fff}
.hero{left:0;top:123px;width:966px;height:462px;background:linear-gradient(160deg,#9a9c9e 0%,#5f6265 40%,#3c3f42 75%,#6b6d6f 100%);box-shadow:0 6px 12px rgba(0,0,0,.25)}
.hero-brand{left:608px;top:163px;font-weight:300;font-size:36px;color:#2a2a2a}
.arrow{width:30px;height:30px;border-radius:50%;background:rgba(40,40,40,.75);top:330px}
.dots{left:475px;top:557px;display:flex;gap:4px}
.dots i{width:11px;height:11px;border:1.5px solid #fff;display:block}
.dots i.on{background:var(--teal)}
.section-title{left:0;width:966px;text-align:center;font-weight:300;font-size:18px;color:#444}
.rule{left:24px;width:919px;height:1px;background:var(--rule)}
.rule-accent{height:1px;background:var(--teal)}
.knot{width:10px;height:10px;border:1.5px solid #999;border-radius:50%;background:#fff}
.card{top:677px;width:175px}
.card .photo{width:175px;height:120px;border-bottom:4px solid var(--teal)}
.card h3{margin-top:13px;text-align:center;font-weight:400;font-size:13px;color:var(--teal-text)}
.card hr{border:0;height:1px;background:var(--rule);margin-top:4px}
.card p{margin-top:9px;text-align:center;font-size:9.3px;line-height:13px;color:var(--grey)}
.btn{display:block;width:70px;height:20px;border:1px solid var(--btn-border);background:var(--btn);font-size:9.5px;color:#666;text-align:center;line-height:18px}
.card .btn{margin:10px auto 0}
.frame{left:24px;top:1033px;width:281px;height:153px;border:1px solid #d4d4d4;padding:5px}
.frame div{width:100%;height:100%;background:linear-gradient(135deg,#6e7072 0%,#8a5a3c 35%,#5c5f62 60%,#c9cbcd 100%)}
.lead{left:335px;top:1036px;width:610px;font-size:12px;line-height:19px;color:var(--teal-text)}
.body-copy{left:335px;top:1080px;width:610px;font-size:10px;line-height:16px;color:#777}
</style>
</head>
<body>

<header>
  <div class="abs brand">Corwick Habitat</div>
  <div class="abs contact" style="top:30px">
    <svg width="12" height="10" viewBox="0 0 12 10"><path d="M1 3 Q6 -1 11 3 L10 4.5 L8 3.5 L8 2.5 Q6 2 4 2.5 L4 3.5 L2 4.5Z M3 5 L9 5 L10 9.5 L2 9.5Z" fill="#468a8e"/></svg>
    (02) 9000 4417
  </div>
  <div class="abs contact" style="top:51px">
    <svg width="12" height="9" viewBox="0 0 12 9"><rect x=".5" y=".5" width="11" height="8" fill="none" stroke="#468a8e"/><path d="M.5 .5 L6 5 L11.5 .5" fill="none" stroke="#468a8e"/></svg>
    info@corwickhabitat.com.au
  </div>
</header>

<nav class="abs nav">
  <a style="left:60px">Home</a><span class="sep" style="left:109px"></span>
  <a style="left:128px">About us</a><span class="sep" style="left:191px"></span>
  <a style="left:214px">Recent Projects</a><span class="sep" style="left:311px"></span>
  <a style="left:331px">Our Services</a><span class="sep" style="left:411px"></span>
  <a style="left:433px">Contact Us</a>
</nav>
<div class="abs search"><span>Search..</span><div class="go">
  <svg width="19" height="15" viewBox="0 0 19 15"><circle cx="8" cy="6" r="3" fill="none" stroke="#468a8e" stroke-width="1.5"/><path d="M10 8 L13 11" stroke="#468a8e" stroke-width="2"/></svg>
</div></div>

<div class="abs hero" role="img" aria-label="Photo of a modern commercial building with grey louvred facade and a teal sign panel"></div>
<svg class="abs" style="left:67px;top:123px" width="14" height="7"><path d="M0 0 L14 0 L7 7Z" fill="#fff"/></svg>
<div class="abs hero-brand">Corwick Habitat</div>
<svg class="abs arrow" style="left:8px" viewBox="0 0 30 30"><circle cx="15" cy="15" r="15" fill="rgba(40,40,40,.75)"/><path d="M17 9 L11 15 L17 21" fill="none" stroke="#fff" stroke-width="2.5"/></svg>
<svg class="abs arrow" style="left:928px" viewBox="0 0 30 30"><circle cx="15" cy="15" r="15" fill="rgba(40,40,40,.75)"/><path d="M13 9 L19 15 L13 21" fill="none" stroke="#fff" stroke-width="2.5"/></svg>
<div class="abs dots"><i class="on"></i><i></i><i></i><i></i></div>

<h2 class="abs section-title" style="top:611px">We specialise in the internal fit outs to</h2>
<div class="abs rule" style="top:642px"></div>
<div class="abs rule-accent" style="left:333px;top:642px;width:135px"></div>
<div class="abs rule-accent" style="left:490px;top:642px;width:144px"></div>
<div class="abs knot" style="left:474px;top:637px"></div>

<div class="abs card" style="left:24px">
  <div class="photo" role="img" aria-label="Photo of an industrial office building with glass facade" style="background:linear-gradient(180deg,#8fb3d9 0%,#5a4a44 60%,#3c3c3c 100%)"></div>
  <h3>Industrial Offices</h3><hr>
  <p>Aliquam erat voltpatis acaturp<br>nteger rutrum kerua delertas</p>
  <span class="btn">Read More</span>
</div>
<div class="abs card" style="left:210px">
  <div class="photo" role="img" aria-label="Photo of a multi storey office building" style="background:linear-gradient(160deg,#b9bbbd 0%,#7d8083 50%,#d5d6d7 100%)"></div>
  <h3>Multi Storey Offices</h3><hr>
  <p>Aliquam erat voltpatis acaturp<br>nteger rutrum kerua delertas</p>
  <span class="btn">Read More</span>
</div>
<div class="abs card" style="left:396px">
  <div class="photo" role="img" aria-label="Photo of a commercial building with louvred facade" style="background:linear-gradient(160deg,#a4a6a8 0%,#55585b 50%,#7b7e80 100%)"></div>
  <h3>Commercial Projects</h3><hr>
  <p>Aliquam erat voltpatis acaturp<br>nteger rutrum kerua delertas</p>
  <span class="btn">Read More</span>
</div>
<div class="abs card" style="left:582px">
  <div class="photo" role="img" aria-label="Photo of a building with timber and grey cladding" style="background:linear-gradient(135deg,#6f7173 0%,#9a5e3a 40%,#5e6164 70%,#bfc1c3 100%)"></div>
  <h3>Residential Houses</h3><hr>
  <p>Aliquam erat voltpatis acaturp<br>nteger rutrum kerua delertas</p>
  <span class="btn">Read More</span>
</div>
<div class="abs card" style="left:770px">
  <div class="photo" role="img" aria-label="Photo of a lobby interior with timber ceiling" style="background:linear-gradient(180deg,#3c3a38 0%,#8a6a48 40%,#d8d4c8 70%,#9a8e6e 100%)"></div>
  <h3>Eternal Facades</h3><hr>
  <p>Aliquam erat voltpatis acaturp<br>nteger rutrum kerua delertas</p>
  <span class="btn">Read More</span>
</div>

<h2 class="abs section-title" style="top:964px">Welcome to Corwick Habitat Pty Ltd</h2>
<div class="abs rule" style="top:996px"></div>
<div class="abs rule-accent" style="left:333px;top:996px;width:135px"></div>
<div class="abs rule-accent" style="left:490px;top:996px;width:144px"></div>
<div class="abs knot" style="left:474px;top:991px"></div>

<div class="abs frame"><div role="img" aria-label="Photo of a building with timber and grey cladding panels"></div></div>
<p class="abs lead">Corwick Habitat Pty Ltd was established in 2005 and has been operating in the Sydney area, but has completed numerous projects outside of Sydney.</p>
<p class="abs body-copy">The key group of our operating staff have all been involved in the construction industry for well over 20 years.<br>Our employees are skilled and trained and have the experience to deliver the best possible product, safely and on time.<br>At Corwick Habitat we pride ourselves on working together with our clients in providing the best possible service on schedule and within budget.</p>
<span class="abs btn" style="left:335px;top:1163px">Read More</span>

</body>
</html>
```